Web Design Project - KornHaus.de

The page shall provide individual brown-bread mix.
There shall be presented:
* RECIPES: consumer's choice and feedback area
* EQUIPMENT: baking equipment store
* BREAD-MIX: individual mix and configurator function for bread-mix
The consumer can search/view the content and checkout the products. A user can establish a profile. A user can interact on the page for feedback on content and connection to social media.
Industry/Entity Type
Store
Look and feel
Each slider illustrates characteristics of the customer's brand and the style your logo design should communicate.

```html
<!DOCTYPE html>
<html lang="en">
<head>
<meta charset="utf-8">
<title>KornHaus.de</title>
<link href="https://fonts.googleapis.com/css2?family=Playball&family=Roboto:wght@300;400;700&family=Crimson+Text&display=swap" rel="stylesheet">
<style>
:root{
  --paper:#e9e4dd;
  --panel:#efece7;
  --brown-dark:#2a1003;
  --brown:#3a1805;
  --gold:#f6c500;
  --orange:#e05f00;
  --text-dark:#2b1406;
  --footer-text:#8a5a3a;
  --footer-bottom:#1e0b02;
}
*{margin:0;padding:0;box-sizing:border-box}
html,body{width:960px;height:1200px;overflow:hidden}
body{background:var(--paper);font-family:'Roboto',Arial,sans-serif;color:var(--text-dark);position:relative}
.abs{position:absolute}
.script{font-family:'Playball',cursive}
.serif{font-family:'Crimson Text',Georgia,serif}

/* top bar */
.top-links{top:14px;display:flex;gap:22px;font-size:12px;font-weight:300;color:#2b1406}
.top-links span::before{content:"";display:inline-block;width:4px;height:4px;border-radius:50%;background:#2b1406;margin-right:6px;vertical-align:middle}
.cart-badge{left:828px;top:0;width:43px;height:50px}
.cart-badge-count{left:828px;top:6px;width:43px;text-align:center;color:#fff;font-size:20px;font-weight:700}

/* brand name */
.brand-name{left:280px;top:74px;width:400px;text-align:center;color:var(--brown);font-size:38px;font-weight:700;line-height:44px}

.main-nav{left:0;top:140px;width:960px;height:46px;background:var(--brown-dark);border-top:2px solid var(--gold);border-bottom:2px solid var(--gold)}
.nav-item,.nav-sep{top:13px;color:#fff;font-size:13px;font-weight:300}
.search-field{left:631px;top:8px;width:177px;height:28px;border:1px solid #5c3416;background:#2a1003;color:#6b4a32;font-size:9px;padding:8px 6px}
.search-btn{left:811px;top:8px;width:60px;height:28px;background:var(--gold);color:#2b1406;font-size:12px;text-align:center;line-height:28px}

/* hero */
.hero-panel{left:23px;top:186px;width:909px;height:324px;background:var(--panel)}
.hero-frame{left:89px;top:211px;width:782px;height:275px;background:var(--brown-dark)}
.hero-inner{left:98px;top:221px;width:370px;height:255px;background:#f2efea}
.hero-photo{left:468px;top:221px;width:394px;height:255px;background:linear-gradient(135deg,#8a5a30 0%,#c79a63 40%,#9a6a3c 70%,#5e3a1a 100%)}
.hero-title{left:132px;top:254px;font-size:44px;color:var(--text-dark);line-height:1}
.hero-sub{left:132px;top:302px;font-size:17px;color:var(--text-dark)}
.hero-text{left:132px;top:346px;width:300px;font-size:12.5px;line-height:15px;color:var(--text-dark)}
.shop-btn{left:132px;top:401px;width:134px;height:43px;background:linear-gradient(#ee7a1c,#d45500);border:1px solid #b94600;color:#fff;font-size:26px;text-align:center;line-height:40px;box-shadow:0 2px 3px rgba(0,0,0,.25)}

.section-title{top:552px;font-size:28px;color:var(--text-dark)}

/* product cards */
.product-card{top:603px;width:178px;height:244px;background:#f2efea;border:1px solid #dcd6ce;border-radius:5px;overflow:hidden}
.product-image{position:absolute;left:0;top:15px;width:176px;height:119px;background:#fff}
.product-image div{position:absolute;left:18px;top:10px;width:140px;height:98px;border-radius:40px 30px 20px 20px;background:radial-gradient(ellipse at 40% 40%,#a6774c,#7a4e2c 60%,#c49a6e 100%)}
.product-desc{position:absolute;left:11px;top:150px;width:160px;font-size:12px;line-height:16px}
.product-price{position:absolute;left:11px;top:194px;font-size:30px}
.add-btn{top:872px;width:110px;height:24px;background:linear-gradient(90deg,#2a1003 60%,#6b3a18);color:#fff;font-size:10px;font-weight:700;line-height:24px;padding-left:8px}
.add-btn b{font-size:14px;margin-right:8px;font-weight:700}

/* cart widget */
.cart-box{left:694px;top:603px;width:177px;height:190px;background:var(--brown-dark);border-radius:6px}
.cart-count{left:795px;top:626px;color:#fff;font-size:10px}
.cart-row{left:706px;width:152px;height:23px;background:#5b3a2a;border:1px solid #6e4a38;color:#fff;font-size:10px;line-height:21px;padding:0 6px;display:flex;justify-content:space-between}
.cart-btn{left:706px;width:97px;height:23px;font-size:10px;font-weight:700;line-height:23px;padding-left:7px}

/* footer */
.footer{left:0;top:944px;width:960px;height:206px;background:var(--brown-dark)}
.footer-bottom{left:0;top:1150px;width:960px;height:50px;background:var(--footer-bottom)}
.footer-title{left:89px;top:984px;font-size:28px;color:#fff}
.info-link{width:172px;font-size:10px;color:var(--footer-text);padding-bottom:9px;border-bottom:1px dashed #5c3416}
.info-link.last{border-bottom:none}
.info-link::before{content:"";display:inline-block;width:4px;height:4px;border-radius:50%;background:var(--footer-text);margin-right:5px;vertical-align:middle}
.delivery-title{left:491px;top:980px;font-size:44px;color:var(--orange)}
.delivery-sub{left:491px;top:1038px;font-size:18px;color:#fff;font-weight:700}
.delivery-sub strong{font-size:26px}
.delivery-text{left:491px;top:1074px;width:310px;font-size:10px;line-height:16px;color:var(--footer-text)}
.social-ribbon{left:828px;top:944px;width:43px;height:167px}
.bottom-links{left:89px;top:1170px;font-size:10px;color:var(--footer-text);white-space:nowrap}
.bottom-links span{margin:0 6px}
.copyright{left:571px;top:1170px;width:300px;text-align:right;font-size:10px;color:var(--footer-text);white-space:nowrap}
.copyright em{font-style:normal;color:#e8d8c8}
</style>
</head>
<body>

<div class="abs top-links" style="left:89px"><span>Home</span><span>Sitemap</span><span>Contact</span></div>
<div class="abs top-links" style="left:624px"><span>My Account</span><span>Shopping Cart</span></div>
<svg class="abs cart-badge" viewBox="0 0 43 50"><polygon points="0,0 43,0 43,50 21.5,40 0,50" fill="#e05f00"/></svg>
<div class="abs cart-badge-count">0</div>

<div class="abs brand-name">KornHaus.de</div>

<nav class="abs main-nav">
  <span class="abs nav-item" style="left:89px">About Us</span>
  <span class="abs nav-sep" style="left:167px">|</span>
  <span class="abs nav-item" style="left:199px">Recipes</span>
  <span class="abs nav-sep" style="left:274px">|</span>
  <span class="abs nav-item" style="left:306px">Equipment</span>
  <span class="abs nav-sep" style="left:394px">|</span>
  <span class="abs nav-item" style="left:426px">Bread-Mix</span>
  <div class="abs search-field">type your text here</div>
  <div class="abs search-btn">Search</div>
</nav>

<div class="abs hero-panel"></div>
<div class="abs hero-frame"></div>
<div class="abs hero-inner"></div>
<div class="abs hero-photo" role="img" aria-label="Photo of assorted rustic bread loaves in a wicker basket on a wooden table"></div>
<h1 class="abs hero-title script">Lorem ipsum</h1>
<div class="abs hero-sub script">dolor sit amet, consectetur adipisicing elit</div>
<p class="abs hero-text serif">Sed ut perspiciatis unde omnis iste natus error sit volupta-tem accusantium doloremque laudantium.</p>
<div class="abs shop-btn script">Shop now</div>

<h2 class="abs section-title script" style="left:89px">Featured Products</h2>

<div class="abs product-card" style="left:89px">
  <div class="product-image" role="img" aria-label="Photo of sliced wholegrain bread loaf"><div></div></div>
  <p class="product-desc serif">Sed ut perspiciatis unde omnis iste natus error sit</p>
  <div class="product-price serif">€ 2.00</div>
</div>
<div class="abs product-card" style="left:290px">
  <div class="product-image" role="img" aria-label="Photo of sliced wholegrain bread loaf"><div></div></div>
  <p class="product-desc serif">Sed ut perspiciatis unde omnis iste natus error sit</p>
  <div class="product-price serif">€ 2.00</div>
</div>
<div class="abs product-card" style="left:492px">
  <div class="product-image" role="img" aria-label="Photo of sliced wholegrain bread loaf"><div></div></div>
  <p class="product-desc serif">Sed ut perspiciatis unde omnis iste natus error sit</p>
  <div class="product-price serif">€ 2.00</div>
</div>

<div class="abs add-btn" style="left:89px"><b>+</b>Add to cart</div>
<div class="abs add-btn" style="left:290px"><b>+</b>Add to cart</div>
<div class="abs add-btn" style="left:492px"><b>+</b>Add to cart</div>

<h2 class="abs section-title script" style="left:694px">Shopping Cart</h2>
<div class="abs cart-box"></div>
<svg class="abs" style="left:705px;top:617px" width="20" height="17" viewBox="0 0 20 17">
  <path d="M6,7 L10,1 L14,7" fill="none" stroke="#fff" stroke-width="2"/>
  <path d="M1,7 H19 L17,16 H3 Z" fill="#fff"/>
  <path d="M7,9 V14 M10,9 V14 M13,9 V14" stroke="#2a1003" stroke-width="1.5"/>
</svg>
<div class="abs cart-count">0 Products</div>
<div class="abs cart-row" style="top:651px"><span>Shipping</span><span>$0.00</span></div>
<div class="abs cart-row" style="top:678px"><span>Total</span><span>$0.00</span></div>
<div class="abs cart-btn" style="top:719px;background:var(--gold);color:#2b1406">Cart</div>
<div class="abs cart-btn" style="top:746px;background:var(--orange);color:#fff">Check out</div>

<footer>
  <div class="abs footer"></div>
  <h2 class="abs footer-title script">More Info</h2>
  <div class="abs" style="left:89px;top:1033px">
    <div class="info-link">Shipping Information</div>
    <div class="info-link" style="margin-top:10px">Order Status</div>
    <div class="info-link last" style="margin-top:10px">Our Guarantees</div>
  </div>
  <div class="abs" style="left:290px;top:1033px">
    <div class="info-link">Shipping Information</div>
    <div class="info-link" style="margin-top:10px">Order Status</div>
    <div class="info-link last" style="margin-top:10px">Our Guarantees</div>
  </div>
  <div class="abs delivery-title script">Free delivery</div>
  <div class="abs delivery-sub">on orders over €<strong>49</strong>.99</div>
  <p class="abs delivery-text">Sed ut perspiciatis unde omnis iste natus error sit voluptatem accus-antium doloremque laudantium, totam rem aperiam</p>
  <svg class="abs social-ribbon" viewBox="0 0 43 167">
    <polygon points="0,0 43,0 43,167 21.5,156 0,167" fill="#f6c500"/>
    <circle cx="21.5" cy="35" r="12" fill="#3a1805" stroke="#fff" stroke-width="1.5"/>
    <circle cx="21.5" cy="67" r="12" fill="#3a1805" stroke="#fff" stroke-width="1.5"/>
    <circle cx="21.5" cy="99" r="12" fill="#3a1805" stroke="#fff" stroke-width="1.5"/>
    <circle cx="21.5" cy="131" r="12" fill="#3a1805" stroke="#fff" stroke-width="1.5"/>
  </svg>
  <div class="abs footer-bottom"></div>
  <div class="abs bottom-links">Home<span>|</span>About Us<span>|</span>Contact Us<span>|</span>Privacy &amp; Security Policy<span>|</span>Terms of Use</div>
  <div class="abs copyright">Copyright © 2011 <em>KornHaus</em>. All rights reserved.</div>
</footer>

</body>
</html>
```